Business card for Property Management consultant

I need a business card for my business LX Vantage - I consult to real estate agents to improve the performance of their Property Management departments (rental houses management). The card needs to be very professional looking, incorporating our logo and my photo plus the line "Develop your Rent Roll to Perform"

Target Market(s)

Real Estate business owners

Industry/Entity Type

Business Consultant

Contact Information for Business Card

Business name - LX Vantage (logo uploaded)
My Name : Marcia Kellaway -
Title : Property Management Consultant

Develop your Rent Roll to perform

Phone : +61 438592716
email : marcia@lxvantage.com.au
website ; www.lxvantage.com.au

Requirements
Must have
• Logo
• My photo
• Very corporate / professional look

```html
<!DOCTYPE html>
<html lang="en">
<head>
<meta charset="utf-8">
<title>LX Vantage – Business Card</title>
<link rel="stylesheet" href="https://fonts.googleapis.com/css2?family=Questrial&display=swap">
<style>
  :root {
    --page: #e4e4e6;
    --card-dark: #262626;
    --card-dark-2: #1c1c1c;
    --card-light: #ffffff;
    --band-light: #d6d6d6;
    --band-dark: #a9a9a9;
    --ink: #333333;
    --ink-soft: #f2f2f2;
    --brand-blue: #3f5fb5;
    --brand-sky: #3aa6cc;
    --photo-a: #3a63c9;
    --photo-b: #c9c9cc;
  }
  * { margin: 0; padding: 0; box-sizing: border-box; }
  html, body { width: 1200px; height: 900px; overflow: hidden; }
  body {
    background: var(--page);
    font-family: "Questrial", "Century Gothic", sans-serif;
    display: flex;
    flex-direction: column;
    align-items: center;
    justify-content: center;
    gap: 50px;
  }
  .card {
    width: 600px;
    height: 333px;
    position: relative;
    overflow: hidden;
    box-shadow: 0 10px 28px rgba(0,0,0,0.25);
  }

  /* Back */
  .card-back {
    background: linear-gradient(180deg, var(--card-dark), var(--card-dark-2));
    display: flex;
    flex-direction: column;
    align-items: center;
    justify-content: center;
    gap: 34px;
  }
  .brand {
    display: flex;
    align-items: center;
    gap: 14px;
    font-size: 46px;
    letter-spacing: 1px;
    line-height: 1;
  }
  .brand-mark {
    width: 30px;
    height: 30px;
    background: var(--brand-blue);
  }
  .card-back .brand { color: var(--ink-soft); }
  .back-web {
    color: var(--ink-soft);
    font-size: 17px;
    letter-spacing: 0.5px;
  }

  /* Front */
  .card-front { background: var(--card-dark); }
  .front-top {
    position: absolute;
    left: 0; top: 0;
    width: 100%; height: 178px;
    background: var(--card-light);
  }
  .front-top .brand {
    position: absolute;
    left: 40px; top: 78px;
    font-size: 44px;
    color: var(--ink);
  }
  .tagline-band {
    position: absolute;
    left: 0; top: 178px;
    width: 100%; height: 30px;
    background: linear-gradient(90deg, var(--band-light), var(--band-dark));
    display: flex;
    align-items: center;
    padding-left: 40px;
  }
  .tagline {
    color: #f7f7f7;
    font-size: 13px;
    letter-spacing: 1.2px;
    text-transform: uppercase;
  }
  .portrait {
    position: absolute;
    right: 24px; top: 22px;
    width: 168px; height: 196px;
    border: 4px solid #ffffff;
    background: linear-gradient(180deg, var(--photo-b) 0%, #e7e7e9 45%, var(--photo-a) 100%);
    box-shadow: 0 2px 6px rgba(0,0,0,0.25);
  }
  .identity {
    position: absolute;
    right: 24px; top: 236px;
    text-align: right;
  }
  .identity-name {
    color: var(--brand-blue);
    font-size: 19px;
    letter-spacing: 0.6px;
    text-transform: uppercase;
  }
  .identity-title {
    color: var(--ink-soft);
    font-size: 14px;
    margin-top: 4px;
  }
  .contacts {
    position: absolute;
    left: 40px; top: 238px;
    list-style: none;
    display: flex;
    flex-direction: column;
    gap: 9px;
  }
  .contacts li {
    display: flex;
    align-items: center;
    gap: 10px;
    color: var(--ink-soft);
    font-size: 14px;
    letter-spacing: 0.3px;
  }
  .contact-icon {
    width: 18px; height: 18px;
    background: var(--brand-blue);
    border-radius: 3px;
    display: flex;
    align-items: center;
    justify-content: center;
  }
  .contact-icon svg { width: 12px; height: 12px; }
</style>
</head>
<body>

  <section class="card card-back" aria-label="Business card back">
    <div class="brand"><span class="brand-mark"></span><span>LX Vantage</span></div>
    <p class="back-web">www.lxvantage.com.au</p>
  </section>

  <section class="card card-front" aria-label="Business card front">
    <div class="front-top">
      <div class="brand"><span class="brand-mark"></span><span>LX Vantage</span></div>
    </div>
    <div class="tagline-band"><p class="tagline">Develop your Rent Roll to Perform</p></div>
    <div class="portrait" role="img" aria-label="Portrait photo of Marcia Kellaway"></div>
    <div class="identity">
      <p class="identity-name">Marcia Kellaway</p>
      <p class="identity-title">Property Management Consultant</p>
    </div>
    <ul class="contacts">
      <li>
        <span class="contact-icon">
          <svg viewBox="0 0 12 12"><path d="M3 1 L5 3 L4 4.5 Q5 7 7.5 8 L9 7 L11 9 L9.5 11 Q3 10 1 2.5 Z" fill="#fff"/></svg>
        </span>
        +61 438592716
      </li>
      <li>
        <span class="contact-icon">
          <svg viewBox="0 0 12 12"><rect x="1" y="2.5" width="10" height="7" fill="none" stroke="#fff" stroke-width="1.2"/><path d="M1 3 L6 7 L11 3" fill="none" stroke="#fff" stroke-width="1.2"/></svg>
        </span>
        marcia@lxvantage.com.au
      </li>
      <li>
        <span class="contact-icon">
          <svg viewBox="0 0 12 12"><circle cx="6" cy="6" r="4.8" fill="none" stroke="#fff" stroke-width="1.1"/><ellipse cx="6" cy="6" rx="2" ry="4.8" fill="none" stroke="#fff" stroke-width="1"/><line x1="1.2" y1="6" x2="10.8" y2="6" stroke="#fff" stroke-width="1"/></svg>
        </span>
        www.lxvantage.com.au
      </li>
    </ul>
  </section>

</body>
</html>
```